Lernoptic.com Business Card Design Project

We need a new business card design for our new online company that delivers online education. It initially focused on SEO training but will soon offer more. The design should be fresh and trendy and take into account the colors and website design attached.
Industry/Entity Type
Training

```html
<!DOCTYPE html>
<html lang="en">
<head>
<meta charset="utf-8">
<title>Lernoptic Business Card</title>
<link href="https://fonts.googleapis.com/css2?family=Arimo:wght@400;700&display=swap" rel="stylesheet">
<style>
  :root {
    --backdrop-center: #f6f7f6;
    --backdrop-edge: #e3e4e4;
    --brand-green: #679b3a;
    --ink: #231f20;
    --card-white: #ffffff;
    --card-border: #8a8a8a;
  }
  * { margin: 0; padding: 0; box-sizing: border-box; }
  html, body {
    width: 1200px;
    height: 900px;
    overflow: hidden;
  }
  body {
    position: relative;
    background: radial-gradient(ellipse at 50% 45%, var(--backdrop-center) 0%, var(--backdrop-edge) 100%);
    font-family: "Arimo", Arial, sans-serif;
    color: var(--ink);
  }
  .business-card {
    position: absolute;
    left: 237px;
    top: 242px;
    width: 726px;
    height: 416px;
    background: var(--card-white);
    border: 1px solid var(--card-border);
  }
  .brand-panel {
    position: absolute;
    left: 0;
    top: 0;
    width: 241px;
    height: 100%;
    background: var(--brand-green);
  }
  .brand-panel-square {
    position: absolute;
    left: 85px;
    top: 300px;
    width: 70px;
    height: 70px;
    background: var(--card-white);
  }
  .wordmark {
    position: absolute;
    right: 24px;
    top: 30px;
    display: flex;
    align-items: center;
    gap: 14px;
  }
  .wordmark-square {
    width: 42px;
    height: 42px;
    background: var(--brand-green);
  }
  .wordmark-name {
    font-size: 44px;
    font-weight: 400;
    color: var(--ink);
    letter-spacing: 0.5px;
    line-height: 1;
  }
  .holder {
    position: absolute;
    right: 17px;
    top: 172px;
    text-align: right;
    font-size: 19px;
    line-height: 27px;
  }
  .holder-name { font-weight: 700; color: var(--ink); }
  .holder-title { color: var(--brand-green); }
  .contact-block {
    position: absolute;
    top: 305px;
    font-size: 16px;
    line-height: 20px;
    color: var(--ink);
  }
  .contact-address { left: 260px; }
  .contact-lines { right: 17px; text-align: right; }
  .contact-rule {
    position: absolute;
    left: 260px;
    right: 17px;
    top: 369px;
    height: 3px;
    background: var(--brand-green);
  }
  .contact-web {
    position: absolute;
    left: 260px;
    right: 17px;
    top: 378px;
    text-align: center;
    font-size: 18px;
    color: var(--brand-green);
  }
</style>
</head>
<body>
  <section class="business-card">
    <div class="brand-panel">
      <div class="brand-panel-square"></div>
    </div>

    <div class="wordmark">
      <span class="wordmark-square"></span>
      <span class="wordmark-name">lernoptic</span>
    </div>

    <div class="holder">
      <p class="holder-name">Name Lastname</p>
      <p class="holder-title">Designation</p>
    </div>

    <address class="contact-block contact-address" style="font-style: normal;">
      123 Streetname,<br>
      Province, 333333<br>
      Country
    </address>

    <div class="contact-block contact-lines">
      Phone: 000-000-0000<br>
      Fax: 000-000-0000<br>
      email: name@domain.com
    </div>

    <div class="contact-rule"></div>
    <p class="contact-web">www.website.com</p>
  </section>
</body>
</html>
```